Innovative psychologist for companies seeks web design for website

Psychologist offers 2 topics:
1. What can a company do to ensure that employees are satisfied and enjoy their work?
The following explanatory video is linked on the website:
https://www.vidplumora.com/watch?v=qTr8ZpLmW3d
2. How can you successfully change your own behavior?
Explanatory video: https://www.vidplumora.com/watch?v=HxK2vQeRt7b&t=6s
The slogan for the second theme will be: YOU are the pirate of your life!

Target Market(s)

companies and private individuals

Number of Pages Required

1 page

Requirements
Nice to have
• Characteristics of the psychologist: pragmatic, down-to-earth, honest, direct, appreciative, enjoys life, loves nature

```html
<!DOCTYPE html>
<html lang="en">
<head>
<meta charset="utf-8">
<title>Jonas Berwick – Psychologist</title>
<link href="https://fonts.googleapis.com/css2?family=Montserrat:wght@400;500;600;700&display=swap" rel="stylesheet">
<style>
:root{
  --navy:#184a8a;
  --hero:#2f5f93;
  --ink:#1b1b1b;
  --body:#555a61;
  --paper:#fbfbfb;
  --mist:#f0f0f3;
  --line:#c9ccd2;
  --white:#ffffff;
}
*{margin:0;padding:0;box-sizing:border-box}
html,body{width:1200px;height:3140px;overflow:hidden}
body{font-family:'Montserrat',sans-serif;background:var(--paper);color:var(--ink);position:relative}
a{color:inherit;text-decoration:none}
.wrap{position:absolute;left:0;width:1200px}

/* header */
.site-header{top:0;height:85px;background:var(--white);border-bottom:1px solid #e4e4e4}
.brand{position:absolute;left:112px;top:25px;font-size:28px;font-weight:500;color:var(--ink);letter-spacing:.5px}
.main-nav{position:absolute;right:112px;top:31px;display:flex;font-size:16px;color:#333}
.main-nav a{padding:0 20px}
.main-nav a:last-child{padding-right:0}
.main-nav span{color:#444}
.main-nav .active{color:var(--navy);font-weight:700;padding-left:0}

/* hero */
.hero{top:85px;height:470px;background:linear-gradient(100deg,#2c5b8e,#3a6a9e 60%,#2f5f93)}
.hero h1{position:absolute;left:112px;top:100px;width:520px;font-size:42px;line-height:51px;font-weight:600;color:var(--white)}
.hero p{position:absolute;left:112px;top:220px;width:440px;font-size:17px;line-height:26px;color:var(--white)}
.btn-light{position:absolute;left:112px;top:318px;width:158px;height:41px;background:var(--white);color:var(--navy);font-size:17px;display:flex;align-items:center;justify-content:center}
.hero-art{position:absolute;left:570px;top:0;width:630px;height:470px;background:radial-gradient(circle at 295px 225px,#f2828a 0 118px,#fff 119px 140px,#7795b9 141px 182px,transparent 183px)}

/* about */
.about{top:555px;height:575px}
.about-photo{position:absolute;left:72px;top:85px}
.about h2{position:absolute;left:631px;top:75px;font-size:36px;font-weight:600;color:var(--navy)}
.about h3{position:absolute;left:631px;top:133px;font-size:24px;font-weight:500}
.about .copy{position:absolute;left:631px;top:172px;width:457px;font-size:14.4px;line-height:22.3px;color:var(--body);text-align:justify}
.about .copy p+p{margin-top:10px}
.btn-navy{position:absolute;left:631px;top:447px;width:159px;height:41px;background:var(--navy);color:var(--white);font-size:17px;display:flex;align-items:center;justify-content:center}

/* topics */
.topics{top:1130px;height:825px;background:var(--mist)}
.topic h2{position:absolute;font-size:37px;line-height:46px;font-weight:600;color:var(--navy)}
.topic p{position:absolute;width:510px;font-size:14.2px;line-height:22.3px;color:var(--body);text-align:justify}
.video-card{position:absolute;width:354px;height:267px;background:var(--white);box-shadow:0 4px 14px rgba(0,0,0,.12)}
.video-card .art{position:absolute;inset:20px 12px;}
.backdrop{position:absolute;background:var(--navy)}
.play{position:absolute;left:50%;top:50%;width:70px;height:70px;margin:-35px 0 0 -35px;border-radius:50%;background:#0b0b0b;display:block}
.play svg{position:absolute;left:26px;top:21px}

/* testimonials */
.clients{top:1955px;height:390px}
.section-title{position:absolute;left:0;width:1200px;text-align:center;font-size:37px;font-weight:600;color:var(--navy)}
.quote-card{position:absolute;top:165px;width:490px;height:100px}
.quote-mark{position:absolute;left:0;top:-20px;font-size:96px;font-weight:700;color:var(--navy);line-height:1}
.quote-card h4{position:absolute;left:55px;top:14px;font-size:25px;font-weight:500}
.quote-card p{position:absolute;left:55px;top:54px;width:282px;font-size:13px;line-height:18px;color:var(--body);text-align:justify}
.avatar{position:absolute;right:0;top:0;width:96px;height:96px;border-radius:50%;background:radial-gradient(circle at 50% 40%,#9aa4ae,#3e4650)}
.dots{position:absolute;top:335px;left:565px;display:flex;gap:9px}
.dots i{width:17px;height:17px;border-radius:50%;background:#c4c6ca}
.dots i:first-child{background:var(--navy)}
.rule{position:absolute;left:112px;width:976px;height:1px;background:var(--line)}

/* blog */
.blog{top:2345px;height:597px}
.blog .lead{position:absolute;left:0;top:110px;width:1200px;text-align:center;font-size:15.5px;line-height:22px;color:#444}
.post{position:absolute;top:177px;width:308px}
.post .thumb{height:193px}
.post h5{margin-top:20px;font-size:18px;line-height:26px;font-weight:600}
.post p{margin-top:15px;font-size:13.5px;line-height:19.5px;color:var(--body);text-align:justify}

/* footer */
.site-footer{top:2942px;height:198px;background:var(--navy);color:var(--white)}
.site-footer .brand-foot{position:absolute;left:0;top:37px;width:1200px;text-align:center;font-size:30px;font-weight:500;letter-spacing:.5px}
.foot-nav{position:absolute;left:0;top:102px;width:1200px;display:flex;justify-content:center;font-size:17px;font-weight:500}
.foot-nav a{padding:0 36px}
.site-footer .rule{top:150px;background:rgba(255,255,255,.45)}
.copyright{position:absolute;left:0;top:170px;width:1200px;text-align:center;font-size:13.5px;color:#c9d6ea}
</style>
</head>
<body>

<header class="wrap site-header">
  <div class="brand">Jonas Berwick</div>
  <nav class="main-nav">
    <a class="active" href="#">Home</a><span>|</span>
    <a href="#">About Us</a><span>|</span>
    <a href="#">Services</a><span>|</span>
    <a href="#">Blog</a><span>|</span>
    <a href="#">Contact Us</a>
  </nav>
</header>

<section class="wrap hero">
  <h1>You Are The Pirate Of Your Life!</h1>
  <p>Lorem ipsum dolor sit amet, consectetur adipiscing elit, sed do eiusmod tempor incididunt ut labore et dolore magna aliqua.</p>
  <a class="btn-light" href="#">Get Started</a>
  <div class="hero-art" role="img" aria-label="Illustration of two hands untangling a knotted string in front of a pink circle"></div>
</section>

<section class="wrap about">
  <svg class="about-photo" width="525" height="410" viewBox="0 0 525 410" role="img" aria-label="Photo of a therapist listening to a client in a counselling session">
    <defs>
      <linearGradient id="sessionTone" x1="0" y1="0" x2="1" y2="1">
        <stop offset="0" stop-color="#9a5a44"/>
        <stop offset=".55" stop-color="#b9a8a4"/>
        <stop offset="1" stop-color="#d8d4d4"/>
      </linearGradient>
    </defs>
    <path d="M250 2 C340 0 420 60 480 120 C530 170 525 260 500 300 C460 370 330 395 180 405 C80 410 5 380 0 290 C-5 200 40 120 110 60 C160 20 200 3 250 2 Z" fill="url(#sessionTone)"/>
    <path d="M380 50 C440 90 500 130 520 200 C528 260 505 310 470 345 C420 385 320 400 150 408 L180 402 C330 392 455 362 500 300 C520 265 520 200 500 160 C470 110 420 75 380 50 Z" fill="#184a8a"/>
  </svg>
  <h2>About Us</h2>
  <h3>Welcome To Jonas Berwick</h3>
  <div class="copy">
    <p>Sed ut perspiciatis unde omnis iste natus error sit voluptatem accusantium doloremque laudantium, totam rem aperiam, eaque ipsa quae ab illo inventore veritatis et quasi architecto beatae vitae dicta sunt explicabo. Nemo enim ipsam voluptatem quia voluptas sit aspernatur aut odit aut fugit, sed quia consequuntur magni dolores eos qui ratione voluptatem sequi nesciunt dolor sit amet, consectetur, adipisci velit, sed quia non numquam eius modi tempora incidunt</p>
    <p>Ut labore et dolore magnam aliquam quaerat voluptatem. Ut enim ad minima veniam,</p>
  </div>
  <a class="btn-navy" href="#">Read More</a>
</section>

<section class="wrap topics">
  <div class="topic">
    <h2 style="left:112px;top:75px;width:570px">What Can A Company Do To Ensure That Employees Are Satisfied &amp; Enjoy Their Work?</h2>
    <p style="left:112px;top:236px">Sed ut perspiciatis unde omnis iste natus error sit voluptatem accusantium doloremque laudantium, totam rem aperiam, eaque ipsa quae ab illo inventore veritatis et quasi architecto beatae vitae dicta sunt explicabo. Nemo enim ipsam voluptatem quia voluptas sit aspernatur aut odit aut fugit, sed quia consequuntur magni dolores eos qui ratione voluptatem sequi nesciunt</p>
    <div class="backdrop" style="left:790px;top:101px;width:297px;height:266px"></div>
    <div class="video-card" style="left:716px;top:84px">
      <div class="art" role="img" aria-label="Explainer video illustration of a workplace, people and a globe" style="background:linear-gradient(90deg,#e8c79a,#8fb8d6 50%,#7fb07a)"></div>
      <a class="play" href="https://www.vidplumora.com/watch?v=qTr8ZpLmW3d" aria-label="Play video"><svg width="24" height="28" viewBox="0 0 24 28"><path d="M0 0 L24 14 L0 28 Z" fill="#fff"/></svg></a>
    </div>
  </div>
  <div class="topic">
    <div class="backdrop" style="left:112px;top:453px;width:297px;height:283px"></div>
    <div class="video-card" style="left:127px;top:453px">
      <div class="art" role="img" aria-label="Explainer video illustration of a maze heart, a garden gate and a sketched brain" style="background:linear-gradient(90deg,#f3e3cf,#8fc3a0 50%,#e6e6e6)"></div>
      <a class="play" href="https://www.vidplumora.com/watch?v=HxK2vQeRt7b&amp;t=6s" aria-label="Play video"><svg width="24" height="28" viewBox="0 0 24 28"><path d="M0 0 L24 14 L0 28 Z" fill="#fff"/></svg></a>
    </div>
    <h2 style="left:553px;top:458px;width:600px">How Can You Successfully Change Your Own Behaviour?</h2>
    <p style="left:553px;top:574px">Sed ut perspiciatis unde omnis iste natus error sit voluptatem accusantium doloremque laudantium, totam rem aperiam, eaque ipsa quae ab illo inventore veritatis et quasi architecto beatae vitae dicta sunt explicabo. Nemo enim ipsam voluptatem quia voluptas sit aspernatur aut odit aut fugit, sed quia consequuntur magni dolores eos qui ratione voluptatem sequi nesciunt</p>
  </div>
</section>

<section class="wrap clients">
  <h2 class="section-title" style="top:78px">What Our Clients Say</h2>
  <div class="quote-card" style="left:112px">
    <div class="quote-mark">“</div>
    <h4>John Peter</h4>
    <p>Lorem ipsum dolor sit amet, consectetur adipiscing elit, sed do eiusmod tempor incididunt ut labore et</p>
    <div class="avatar" role="img" aria-label="Portrait photo of John Peter"></div>
  </div>
  <div class="quote-card" style="left:635px;width:453px">
    <div class="quote-mark">“</div>
    <h4>Thomas Paul</h4>
    <p>Lorem ipsum dolor sit amet, consectetur adipiscing elit, sed do eiusmod tempor incididunt ut labore et</p>
    <div class="avatar" role="img" aria-label="Portrait photo of Thomas Paul" style="background:radial-gradient(circle at 50% 40%,#c2c7cc,#5d7488)"></div>
  </div>
  <div class="dots"><i></i><i></i><i></i></div>
  <div class="rule" style="top:387px"></div>
</section>

<section class="wrap blog">
  <h2 class="section-title" style="top:38px">Latest Blog</h2>
  <p class="lead">Lorem ipsum dolor sit amet, consectetur adipiscing elit, sed do eiusmod<br>dolore magna aliqua. Quis ipsum suspendisse ultrices gravida. Risus commodo viverra maecenas accumsan</p>
  <article class="post" style="left:112px">
    <div class="thumb" role="img" aria-label="Photo of two women talking among green plants" style="background:linear-gradient(120deg,#d9c7a5,#e8e6de 50%,#7f9a6a)"></div>
    <h5>Lorem ipsum dolor sit consectetur adipiscing elit, sed</h5>
    <p>Lorem ipsum dolor sit amet, consectetur adipiscing elit, sed do eiusmod tempor incididunt ut labore et dolore magna</p>
  </article>
  <article class="post" style="left:446px">
    <div class="thumb" role="img" aria-label="Photo of a counsellor in conversation with a young man" style="background:linear-gradient(120deg,#dcdcd6,#b9c2c9 50%,#b86a3e)"></div>
    <h5>Lorem ipsum dolor sit consectetur adipiscing elit, sed</h5>
    <p>Lorem ipsum dolor sit amet, consectetur adipiscing elit, sed do eiusmod tempor incididunt ut labore et dolore magna</p>
  </article>
  <article class="post" style="left:781px">
    <div class="thumb" role="img" aria-label="Photo of a therapist taking notes while listening to a client" style="background:linear-gradient(120deg,#d8c9a0,#8a6a48 55%,#4a3a2c)"></div>
    <h5>Lorem ipsum dolor sit consectetur adipiscing elit, sed</h5>
    <p>Lorem ipsum dolor sit amet, consectetur adipiscing elit, sed do eiusmod tempor incididunt ut labore et dolore magna</p>
  </article>
</section>

<footer class="wrap site-footer">
  <div class="brand-foot">Jonas Berwick</div>
  <nav class="foot-nav">
    <a href="#">Home</a><span>|</span>
    <a href="#">About Us</a><span>|</span>
    <a href="#">Services</a><span>|</span>
    <a href="#">Blog</a><span>|</span>
    <a href="#">Contact Us</a>
  </nav>
  <div class="rule"></div>
  <div class="copyright">Copyright © 2024 Jonas Berwick. All rights reserved.</div>
</footer>

</body>
</html>
```